Business Card Design with new logo

Dorian Pelleway 4172
E 118th St Brenly, IL 60999
Cell: 217-555-0193
pellewayrestoration@mailvane.test

Classic Car Restoration Services Buy Sell Trade Consign

Dorian Pelleway 9698
Cell: 217-555-0193

```html
<!DOCTYPE html>
<html lang="en">
<head>
<meta charset="utf-8">
<title>Pelleway Restoration – Business Card</title>
<link href="https://fonts.googleapis.com/css2?family=Ubuntu:ital,wght@0,400;0,700;1,400&display=swap" rel="stylesheet">
<style>
  :root {
    --backdrop: #d8d5ce;
    --tan: #dcc49d;
    --tan-deep: #d3b88c;
    --paper: #f1f1ef;
    --ink: #222222;
    --ink-soft: #3a3a3a;
    --navy: #1b2a3a;
    --car-tone: #b8a27c;
  }
  * { box-sizing: border-box; margin: 0; padding: 0; }
  html, body {
    width: 1200px; height: 1200px; overflow: hidden;
    background: var(--backdrop);
    font-family: "Ubuntu", sans-serif;
  }
  .card {
    position: absolute; left: 184px; width: 829px; height: 474px;
    overflow: hidden;
    box-shadow: 0 18px 40px rgba(0,0,0,0.18);
  }
  .card--front { top: 50px; }
  .card--back { top: 672px; }
  .card__tan {
    position: absolute; left: 0; top: 0; width: 100%;
    background: linear-gradient(135deg, var(--tan) 0%, var(--tan-deep) 100%);
  }
  .card--front .card__tan { height: 286px; }
  .card--back .card__tan { height: 388px; }
  .card__band {
    position: absolute; left: 0; bottom: 0; width: 100%;
    background: var(--paper);
  }
  .card--front .card__band { height: 188px; }
  .card--back .card__band { height: 86px; }

  .car-art {
    position: absolute; left: 470px; top: 14px; width: 359px; height: 260px;
    background: radial-gradient(ellipse at 60% 60%, var(--car-tone) 0%, rgba(184,162,124,0.35) 60%, rgba(184,162,124,0) 80%);
  }
  .owner-name {
    position: absolute; left: 50px; top: 34px;
    font-size: 49px; font-weight: 700; color: var(--ink); letter-spacing: -0.3px;
    white-space: nowrap;
  }
  .tagline {
    position: absolute; left: 58px; top: 98px;
    font-size: 26px; font-style: italic; line-height: 33px; color: var(--ink-soft);
  }
  .contact-list {
    position: absolute; left: 58px; top: 317px; list-style: none;
  }
  .contact-list li {
    display: flex; align-items: center; height: 45px;
    font-size: 25px; color: var(--ink-soft); white-space: nowrap;
  }
  .contact-list svg { width: 30px; height: 32px; margin-right: 12px; fill: var(--ink-soft); }

  .brand-name {
    position: absolute; left: 0; top: 170px; width: 100%;
    display: flex; justify-content: center; align-items: center; gap: 16px;
    font-size: 42px; font-weight: 700; color: var(--navy);
  }
  .brand-name .dot {
    width: 22px; height: 22px; border-radius: 50%; background: var(--navy);
  }
</style>
</head>
<body>
  <section class="card card--front">
    <div class="card__tan"></div>
    <div class="card__band"></div>
    <div class="car-art" role="img" aria-label="Faint silhouette of a sports car"></div>
    <h1 class="owner-name">Dorian Pelleway 4172</h1>
    <p class="tagline">Classic Car Restoration Services<br>Buy Sell Trade Consign</p>
    <ul class="contact-list">
      <li>
        <svg viewBox="0 0 24 32" aria-hidden="true"><path d="M12 0C5.4 0 0 5.2 0 11.6 0 20 12 32 12 32s12-12 12-20.4C24 5.2 18.6 0 12 0zm0 17a5.5 5.5 0 1 1 0-11 5.5 5.5 0 0 1 0 11z"/></svg>
        E 118th St Brenly, IL 60999
      </li>
      <li>
        <svg viewBox="0 0 24 32" aria-hidden="true"><path d="M6 0h12a3 3 0 0 1 3 3v26a3 3 0 0 1-3 3H6a3 3 0 0 1-3-3V3a3 3 0 0 1 3-3zm0 4v18h12V4zm1 21v2h3v-2zm4 0v2h3v-2zm4 0v2h2v-2z"/></svg>
        217-555-0193
      </li>
      <li>
        <svg viewBox="0 0 32 24" aria-hidden="true"><path d="M0 0h32v24H0zm3 3v1l13 10L29 4V3zm0 5v13h26V8L16 18z"/></svg>
        pellewayrestoration@mailvane.test
      </li>
    </ul>
  </section>

  <section class="card card--back">
    <div class="card__tan"></div>
    <div class="card__band"></div>
    <div class="brand-name"><span class="dot"></span>Pelleway Restoration LLC</div>
  </section>
</body>
</html>
```